Health Reimbursement Ad

I need a banner that explains the health insurance user how Reimbursement works.

I will explain it here, as I need it to explaing brasilian health Reimbursement, and I don't know if it is equal to other countries:
Who has health insurance havs two ways of selecting his doctor. The first is easier, just select the doctor from the guide book from the health insurance and call for an appointment. Then the payment will be done directly from the health insurance to the doctor. This is very easy to accomplish and most choose this method. Problems of this method: have to wait long for an appointment, consults will be faster, doctor earns less, doctor is staff from the health company so he may be influenced by its needs, like less exams for example.
I need to explain and convince the user for the second way: go to any doctor he wants. We ask the health company the value he will be reimbursed for this appointment. We then charge exactly the price that will be reimbursed (this is a very often fear of the user, that we charge more than the value of the Reimbursement), the payment will only be completed when the user is reimbursed.
Advantages of this method: user can select any doctor he wants, doctors will have more appointment times, the doctor will not be influenced by health insurance decisions, the relationship between doctor and patient is healthier and clearer, doctor earns more than the previous method (doctor will be happier, also may spend more time analysing the case), free will and free choice, user pay a lot for health insurance when selecting Reimbursement method the value for his spendings is better, better hospital choices.
The big problem is that there is a general fear of the Reimbursement, like:
If the health company does not reimburse me ?? They have to and doctor can wait to fullfill the payment
If the Reimbursement is only part of the full cost ?? We have chosen to charge the exact amount of the Reimbursement.
It is too much paperwork to make it work !! We do all the paperwork, the patient only need to sit and wait.

Well this is the brasilian health system.
I wish to explain the Reimbursement method. Maybe a infograph.
My website is http://www.verilo.com.br

Target Market(s)

health patients

Industry/Entity Type

Hospital

Requirements
Must have
• I wil need to translate it to portuguese, so it is essential to provide me ways to do that.
Fonts for example.
I have all needed software to finish that (Adobe photoshop and ilustrator)
Nice to have
• Maybe like an inphographic
match My website http://www.verilo.com.br theme
Should not have
• image of disease or poor health

```html
<!DOCTYPE html>
<html lang="en">
<head>
<meta charset="utf-8">
<title>Demystify Brasilian health Reimbursement</title>
<link rel="stylesheet" href="https://fonts.googleapis.com/css2?family=Arimo:ital,wght@0,400;0,700;1,700&display=swap">
<style>
  :root {
    --paper: #ffffff;
    --frame: #c9c9c9;
    --ink: #111111;
    --question: #a3201d;
    --rule: #1a1a1a;
    --scene-light: #f4f6f7;
    --scene-mid: #dfe6ea;
  }
  * { margin: 0; padding: 0; box-sizing: border-box; }
  html, body { width: 1200px; height: 514px; overflow: hidden; background: var(--paper); }
  .banner {
    position: relative;
    width: 1200px;
    height: 514px;
    border: 2px solid var(--frame);
    background: var(--paper);
    font-family: "Arimo", Arial, sans-serif;
    color: var(--ink);
  }
  .network-illustration {
    position: absolute;
    left: 14px; top: 9px;
    width: 436px; height: 420px;
    background: radial-gradient(ellipse at 50% 50%, var(--scene-mid) 0%, var(--scene-light) 70%, var(--paper) 100%);
  }
  .slogan {
    position: absolute;
    left: 60px; top: 432px;
    font-size: 52px;
    font-weight: 700;
    letter-spacing: -0.5px;
  }
  .headline {
    position: absolute;
    left: 462px; width: 710px;
    text-align: center;
  }
  .headline-kicker {
    top: 38px;
    font-size: 39px;
    font-weight: 700;
    font-style: italic;
  }
  .headline-main {
    top: 88px;
    font-size: 74px;
    font-weight: 700;
    letter-spacing: 1px;
  }
  .headline-rule {
    position: absolute;
    left: 466px; top: 181px;
    width: 700px; height: 3px;
    background: var(--rule);
  }
  .faq { position: absolute; left: 466px; top: 212px; width: 710px; list-style: none; }
  .faq-item { margin-bottom: 20px; }
  .faq-question { color: var(--question); font-size: 20px; line-height: 26px; }
  .faq-answer { font-size: 20px; line-height: 28px; padding-left: 28px; margin-top: 6px; }
</style>
</head>
<body>
  <div class="banner">
    <div class="network-illustration" role="img" aria-label="Illustration of a network of doctors and nurses standing on connected circles"></div>
    <p class="slogan">My choice.</p>

    <h2 class="headline headline-kicker">Demystify Brasilian health</h2>
    <h1 class="headline headline-main">REIMBURSEMENT</h1>
    <div class="headline-rule"></div>

    <ul class="faq">
      <li class="faq-item">
        <p class="faq-question">If the health company does not reimburse me ??</p>
        <p class="faq-answer">They have to and doctor can wait to fullfill the payment.</p>
      </li>
      <li class="faq-item">
        <p class="faq-question">If the Reimbursement is only part of the full cost ??</p>
        <p class="faq-answer">We have chosen to charge the exact amount of the Reimbursement.</p>
      </li>
      <li class="faq-item">
        <p class="faq-question">It is too much paperwork to make it work !!</p>
        <p class="faq-answer">We do all the paperwork, the patient only need to sit and wait.</p>
      </li>
    </ul>
  </div>
</body>
</html>
```